Blue Harbor Real Estate Institute

This must be done in word press and I will need about 7 tabs The home page, Information page, Schedule and Cost page which will link to a Email me form, a online registration a about us and location/contact tab Each tab will then open several other pages. The home page will describe different courses that we offer since all the schools are about the same you can get a good ideal by going to plimvar.example or brightkeyrealtycourses.example and looking at their site I would like mine to be similar as the courses are exactly the same but I would like the site to be more modern I also need it to be in word press so I can change it and update the dates as they change I have attached he logo below

Target Market(s)

people interested in getting into real estate and those who need continuing education

Coding

Coded - Design and coding required

Number of Pages Required

5+ page

Font styles to use
Sans Serif

Colors
3276b5

Requirements
Must have
• A page to schedule classes, a tab so the college I am partnering with can link the online courses to the back side, a page that describes the type of classes I offer

```html
<!DOCTYPE html>
<html lang="en">
<head>
<meta charset="utf-8">
<title>Blue Harbor Real Estate Institute</title>
<link href="https://fonts.googleapis.com/css2?family=Poppins:ital,wght@0,400;0,500;0,600;0,700;1,400&family=Dancing+Script:wght@500&display=swap" rel="stylesheet">
<style>
:root{
  --blue:#2175c0;
  --blue-dark:#1b64a6;
  --ink:#111111;
  --text:#555555;
  --grey-box:#58595b;
  --pale:#e8f4fd;
  --footer:#1f1f1f;
  --footer-deep:#181818;
  --white:#ffffff;
}
*{box-sizing:border-box;margin:0;padding:0}
html,body{width:1200px;height:2344px;overflow:hidden}
body{font-family:'Poppins',sans-serif;color:var(--text);background:var(--white);position:relative}
.abs{position:absolute}
a{color:inherit;text-decoration:none}

/* header */
.brand{left:234px;top:22px;display:flex;align-items:center;gap:10px}
.brand-mark{width:26px;height:26px;background:var(--blue)}
.brand-name{font-weight:700;color:var(--blue);font-size:17px;line-height:20px;width:220px}
.contact-item{display:flex;gap:10px;align-items:flex-start;font-size:9px;line-height:15px;color:#555}
.contact-item strong{display:block;font-size:12px;color:#222;font-weight:600;letter-spacing:.5px}
.nav{left:0;top:96px;width:1200px;height:41px;background:var(--blue)}
.nav ul{list-style:none;display:flex;position:absolute;left:236px;top:0;height:41px}
.nav li{height:41px;padding:0 22px;display:flex;align-items:center;color:#fff;font-size:8.5px;font-weight:600;border-right:1px solid rgba(255,255,255,.18);letter-spacing:.2px}
.nav li.active{background:#555a60}

/* hero */
.hero{left:0;top:137px;width:1200px;height:444px;background:linear-gradient(90deg,#8a6a5e 0%,#cfc6bd 25%,#d9d6d1 45%,#4d6fa3 55%,#d7cfc6 72%,#d3b08a 85%,#3b3734 100%)}
.hero-script{left:0;width:1200px;top:270px;text-align:center;font-family:'Dancing Script',cursive;font-size:30px;color:#fff}
.hero-title{left:0;width:1200px;top:318px;text-align:center;font-size:31px;line-height:38px;font-weight:700;color:#fff;text-shadow:0 1px 3px rgba(0,0,0,.35)}
.hero-btn{left:528px;top:420px;width:144px;height:34px;background:#2c2c2c;color:#fff;font-size:10.5px;font-weight:600;display:flex;align-items:center;justify-content:center}
.dot{width:5px;height:5px;border-radius:50%;background:#fff}

.feature{top:532px;height:96px;width:242px;display:flex;align-items:center;padding-left:26px;gap:20px;color:#fff}
.feature.blue{background:var(--blue)}
.feature.grey{background:var(--grey-box)}
.feature h3{font-size:12px;line-height:19px;font-weight:600;letter-spacing:.2px}
.feature span{font-size:8px;text-decoration:underline;display:block;margin-top:4px}

/* why */
.why-title{left:234px;top:664px;font-size:21px;font-weight:600;color:var(--ink)}
.rule{width:25px;height:4px;border-top:1px solid #666;border-bottom:1px solid #666}
.why-text{left:234px;top:737px;width:358px;font-size:8.6px;line-height:15px}
.why-text p{margin-bottom:15px}
.why-photo{left:622px;top:670px;width:344px;height:211px;background:linear-gradient(135deg,#b3a38e 0%,#d9cfc0 40%,#8b3b38 75%,#6e3231 100%)}
.quote-title{left:622px;top:902px;font-size:12px;font-weight:600;color:var(--ink)}
.quote-text{left:622px;top:932px;width:350px;font-size:8.6px;line-height:15px}
.quote-text ul{margin-top:12px;list-style:none}
.quote-text li{position:relative;padding-left:25px;margin-bottom:8px}
.quote-text li::before{content:"";position:absolute;left:10px;top:5px;width:5px;height:5px;border-radius:50%;background:#333}

/* welcome */
.welcome{left:0;top:1144px;width:1200px;height:456px;background:var(--pale)}
.center-title{left:0;width:1200px;text-align:center;font-size:21px;font-weight:600;color:var(--ink)}
.card{top:1288px;width:232px;height:251px;background:#fff;text-align:center;padding-top:28px}
.card h4{font-size:13.5px;font-weight:600;color:var(--ink);margin:14px 0 12px}
.card p{font-size:8.6px;line-height:15px;padding:0 20px}
.card a{display:block;margin-top:14px;font-size:8px;font-weight:600;color:var(--blue)}

/* testimonials */
.testi{top:1731px;width:232px;height:98px;border:1px solid #999;padding:28px 20px 0 44px;font-style:italic;font-size:10.2px;line-height:15px;color:#444;letter-spacing:.2px}
.testi .qm{position:absolute;left:18px;top:24px;font-style:normal;font-size:18px;font-weight:700;color:var(--blue)}
.testi::after{content:"";position:absolute;left:110px;bottom:-6px;width:10px;height:10px;background:#fff;border-right:1px solid #999;border-bottom:1px solid #999;transform:rotate(45deg)}
.author{top:1852px;display:flex;gap:14px;align-items:center}
.avatar{width:32px;height:32px;background:linear-gradient(180deg,#cfc9c4,#4b5466)}
.author b{display:block;color:var(--blue);font-size:10px;font-weight:600;letter-spacing:.4px}
.author span{font-size:9px;color:#666}

/* cta */
.cta{left:234px;top:1938px;width:732px;height:63px;background:var(--blue);color:#fff}
.cta-item{top:0;height:63px;display:flex;align-items:center;gap:12px;font-size:9px;line-height:13px}
.cta-item strong{font-size:13px;font-weight:600;margin-left:14px}
.cta-or{left:352px;top:18px;width:26px;height:26px;border-radius:50%;background:#fff;color:var(--blue);font-size:8px;font-weight:700;display:flex;align-items:center;justify-content:center}
.cta-divider{left:365px;top:0;width:1px;height:63px;background:rgba(255,255,255,.5)}

/* footer */
.footer{left:0;top:2001px;width:1200px;height:343px;background:var(--footer);color:#ddd}
.footer-bottom{left:0;top:2298px;width:1200px;height:46px;background:var(--footer-deep);text-align:center;font-size:8px;line-height:46px;color:#888}
.f-brand{left:234px;top:2046px;display:flex;align-items:center;gap:8px}
.f-brand .brand-name{color:var(--blue);font-size:14px;line-height:17px;width:160px}
.f-about{left:234px;top:2106px;width:230px;font-size:8.6px;line-height:15px;color:#ccc}
.social{top:2220px;width:24px;height:24px;border-radius:50%;border:1px solid #bbb}
.f-head{top:2054px;font-size:10.5px;font-weight:600;color:#fff;letter-spacing:.2px}
.f-links{left:505px;top:2090px;list-style:none;font-size:8.6px;color:#ddd}
.f-links li{height:22.6px;display:flex;align-items:center;gap:10px}
.f-links li::before{content:"";width:8px;height:1px;background:#aaa}
.f-contact{left:636px;font-size:8.6px;line-height:15px;display:flex;gap:12px;align-items:flex-start;color:#ddd}
.f-ico{width:21px;height:21px;background:#555;display:flex;align-items:center;justify-content:center;flex-shrink:0}
.f-news{left:797px;top:2092px;width:170px;font-size:8.6px;line-height:15px;color:#ddd}
.news-form{left:797px;top:2130px;width:169px;height:31px;display:flex}
.news-form .field{flex:1;background:#fff;font-size:8px;color:#777;display:flex;align-items:center;gap:6px;padding-left:11px}
.news-form .send{width:38px;background:var(--blue);display:flex;align-items:center;justify-content:center}
</style>
</head>
<body>

<!-- Header -->
<div class="brand abs">
  <div class="brand-mark"></div>
  <div class="brand-name">Blue Harbor Real Estate Institute</div>
</div>
<div class="contact-item abs" style="left:724px;top:37px">
  <svg width="14" height="19" viewBox="0 0 14 19"><path d="M7 0C3.1 0 0 3.1 0 7c0 5 7 12 7 12s7-7 7-12c0-3.9-3.1-7-7-7zm0 9.5A2.5 2.5 0 1 1 7 4.5a2.5 2.5 0 0 1 0 5z" fill="#2175c0"/></svg>
  <div>123, Street Address,<br>City, Country</div>
</div>
<div class="contact-item abs" style="left:858px;top:37px">
  <svg width="16" height="18" viewBox="0 0 24 24"><path d="M6.6 10.8a15.1 15.1 0 0 0 6.6 6.6l2.2-2.2c.3-.3.7-.4 1-.2 1.1.4 2.3.6 3.6.6.6 0 1 .4 1 1V20c0 .6-.4 1-1 1A17 17 0 0 1 3 4c0-.6.4-1 1-1h3.5c.6 0 1 .4 1 1 0 1.3.2 2.5.6 3.6.1.3 0 .7-.2 1z" fill="#2175c0"/></svg>
  <div>Customer Service<strong>666-123-4567</strong></div>
</div>

<nav class="nav abs">
  <ul>
    <li class="active">HOME</li>
    <li>INFORMATION</li>
    <li>SCHEDULE &amp; COST</li>
    <li>REGISTRATION</li>
    <li>ABOUT US</li>
    <li>LOCATION</li>
    <li>CONTACT</li>
  </ul>
</nav>

<!-- Hero -->
<div class="hero abs" role="img" aria-label="Smiling instructor in a blue shirt presenting to a classroom of adult students"></div>
<div class="hero-script abs">Be the best in your industry!</div>
<h1 class="hero-title abs">Real Estate Continuing<br>Education Classes</h1>
<a class="hero-btn abs">GET STARTED</a>
<div class="dot abs" style="left:653px;top:478px"></div>
<div class="dot abs" style="left:650px;top:524px"></div>

<div class="feature blue abs" style="left:234px">
  <svg width="42" height="42" viewBox="0 0 42 42" fill="none" stroke="#fff" stroke-width="1.4"><rect x="12" y="3" width="27" height="18"/><path d="M16 16l6-5 4 3 8-7"/><circle cx="7" cy="14" r="3"/><path d="M4 30v-9h6v9M10 21l5-3"/><circle cx="16" cy="31" r="2.5"/><circle cx="25" cy="31" r="2.5"/><circle cx="34" cy="31" r="2.5"/><path d="M12 40c0-3 2-5 4-5s4 2 4 5M21 40c0-3 2-5 4-5s4 2 4 5M30 40c0-3 2-5 4-5s4 2 4 5"/></svg>
  <div><h3>WE OFFER ONSITE<br>COURSES</h3><span>CLICK HERE</span></div>
</div>
<div class="feature grey abs" style="left:478px">
  <svg width="42" height="42" viewBox="0 0 42 42" fill="none" stroke="#fff" stroke-width="1.4"><rect x="16" y="2" width="18" height="12" rx="1"/><path d="M20 6h10M20 10h7"/><rect x="3" y="14" width="12" height="9"/><circle cx="22" cy="22" r="3"/><path d="M16 33c0-4 3-6 6-6s6 2 6 6"/><rect x="8" y="33" width="28" height="4"/><path d="M4 40h34"/></svg>
  <div><h3>ONLINE COURSES<br>AVAILABLE</h3><span>CLICK HERE</span></div>
</div>
<div class="feature blue abs" style="left:723px">
  <svg width="42" height="42" viewBox="0 0 42 42" fill="none" stroke="#fff" stroke-width="1.6"><rect x="3" y="6" width="32" height="30" rx="3"/><path d="M3 13h32M10 2v8M18 2v8M26 2v8"/><circle cx="10" cy="20" r="1" fill="#fff"/><circle cx="17" cy="20" r="1" fill="#fff"/><circle cx="24" cy="20" r="1" fill="#fff"/><circle cx="10" cy="27" r="1" fill="#fff"/><circle cx="17" cy="27" r="1" fill="#fff"/><circle cx="31" cy="31" r="8" fill="#2175c0"/><path d="M31 27v4h3"/></svg>
  <div><h3>VIEW CLASS<br>SCHEDULE</h3><span>CLICK HERE</span></div>
</div>

<!-- Why choose -->
<h2 class="why-title abs">Why Choose Blue Harbor?</h2>
<div class="rule abs" style="left:234px;top:706px"></div>
<div class="why-text abs">
  <p>Lorem ipsum dolor sit amet, consectetur adipiscing elit. Aenean tempor orci eget neque fermentum tristique. Vestibulum aliquet libero at justo rutrum, non venenatis quam feugiat. Proin mattis, ligula eu maximus finibus, enim velit lacinia turpis, vel pretium libero ante in augue. Nulla est nulla, cursus at imperdiet et, dapibus vel urna. Morbi dapibus ex mauris, at accumsan mauris imperdiet non. Donec sit amet arcu a metus sagittis auctor dictum sit amet nisi. Suspendisse efficitur consectetur tellus, eu tincidunt velit finibus et. Maecenas sit amet blandit risus.</p>
  <p>Vestibulum at sapien urna. Etiam rhoncus metus at neque ultrices, a blandit nunc sodales. Pellentesque pulvinar volutpat arcu, id sagittis lorem dapibus eget. Curabitur eget vulputate mauris, vitae fringilla felis. Vivamus et quam eget lacus ultrices feugiat. Suspendisse interdum pulvinar tortor, ac interdum est pulvinar quis.</p>
  <p>Phasellus purus tortor, varius at dui sit amet, pretium egestas enim. Praesent at tortor ultricies mi molestie porttitor quis eleifend orci. Etiam dui lorem, pretium sit amet vehicula id, pellentesque vel odio.</p>
  <p>Quisque a suscipit justo, nec scelerisque orci. Aenean ut arcu tincidunt, lobortis lorem consequat, tempor turpis. Nam imperdiet neque et massa convallis porttitor. Aenean nec blandit eros, nec tincidunt nisl. In sem leo, luctus ut orci in, hendrerit hendrerit mauris. Nulla blandit efficitur posuere. Lorem ipsum dolor sit amet, consectetur adipiscing elit.</p>
</div>
<div class="why-photo abs" role="img" aria-label="Teacher helping students working on a laptop at classroom desks"></div>
<h3 class="quote-title abs">“Real Estate is a Blue Harbor”</h3>
<div class="quote-text abs">
  Lorem ipsum dolor sit amet, consectetur adipiscing elit. Aenean tempor orci eget neque fermentum tristique. Vestibulum aliquet libero at justo rutrum, non venenatis quam feugiat.
  <ul>
    <li>Lorem ipsum dolor sit amet, consectetur adipiscing elit. Aenean tempor orci eget neque fermentum tristique.</li>
    <li>Ut blandit velit consequat magna scelerisque, quis ornare.</li>
    <li>Cras hendrerit nunc id ligula elementum pretium.</li>
    <li>Quisque a suscipit justo, nec scelerisque orci.</li>
  </ul>
</div>

<!-- Welcome -->
<div class="welcome abs"></div>
<h2 class="center-title abs" style="top:1192px">Welcome to Blue Harbor Real Estate Institute</h2>
<div class="rule abs" style="left:588px;top:1232px"></div>

<div class="card abs" style="left:234px">
  <svg width="64" height="70" viewBox="0 0 64 70"><path d="M32 2l28 15v36L32 68 4 53V17z" fill="#2175c0"/><circle cx="32" cy="35" r="16" fill="none" stroke="#fff" stroke-width="3"/><rect x="30" y="32" width="4" height="12" fill="#fff"/><circle cx="32" cy="27" r="2.4" fill="#fff"/></svg>
  <h4>Information</h4>
  <p>Lorem ipsum dolor sit amet, consectetur adipiscing elit. Mauris eget rutrum elit. Quisque at orci ut nunc blandit egestas. Pellentesque et purus odio.</p>
  <a>LEARN MORE</a>
</div>
<div class="card abs" style="left:484px">
  <svg width="64" height="70" viewBox="0 0 64 70"><path d="M32 2l28 15v36L32 68 4 53V17z" fill="#2175c0"/><text x="32" y="48" text-anchor="middle" font-family="Poppins,sans-serif" font-weight="700" font-size="36" fill="#fff">$</text></svg>
  <h4>Schedule &amp; Cost</h4>
  <p>Lorem ipsum dolor sit amet, consectetur adipiscing elit. Mauris eget rutrum elit. Quisque at orci ut nunc blandit egestas. Pellentesque et purus odio.</p>
  <a>LEARN MORE</a>
</div>
<div class="card abs" style="left:735px">
  <svg width="64" height="70" viewBox="0 0 64 70"><path d="M32 2l28 15v36L32 68 4 53V17z" fill="#2175c0"/><rect x="20" y="18" width="24" height="32" rx="2" fill="none" stroke="#fff" stroke-width="2"/><rect x="27" y="15" width="10" height="6" fill="#2175c0" stroke="#fff" stroke-width="2"/><circle cx="32" cy="32" r="5" fill="none" stroke="#fff" stroke-width="1.6"/><path d="M29.5 32l2 2 3-3.5M25 42h14" stroke="#fff" stroke-width="1.6" fill="none"/></svg>
  <h4>Registration</h4>
  <p>Lorem ipsum dolor sit amet, consectetur adipiscing elit. Mauris eget rutrum elit. Quisque at orci ut nunc blandit egestas. Pellentesque et purus odio.</p>
  <a>LEARN MORE</a>
</div>

<!-- Testimonials -->
<h2 class="center-title abs" style="top:1649px">What Our Students Have To Say</h2>
<div class="rule abs" style="left:588px;top:1690px"></div>

<div class="testi abs" style="left:234px"><span class="qm">“</span>Lorem ipsum dolor sit amet, consectetur adipiscing elit. Ut consectetur facilisis ultricies.</div>
<div class="testi abs" style="left:484px"><span class="qm">“</span>Lorem ipsum dolor sit amet, consectetur adipiscing elit. Ut consectetur facilisis ultricies.</div>
<div class="testi abs" style="left:735px"><span class="qm">“</span>Lorem ipsum dolor sit amet, consectetur adipiscing elit. Ut consectetur facilisis ultricies.</div>

<div class="author abs" style="left:300px"><div class="avatar" role="img" aria-label="Client portrait"></div><div><b>John Smith</b><span>Client</span></div></div>
<div class="author abs" style="left:550px"><div class="avatar" role="img" aria-label="Client portrait"></div><div><b>John Smith</b><span>Client</span></div></div>
<div class="author abs" style="left:800px"><div class="avatar" role="img" aria-label="Client portrait"></div><div><b>John Smith</b><span>Client</span></div></div>

<!-- Call to action -->
<div class="cta abs">
  <div class="cta-item abs" style="left:62px">
    <svg width="12" height="20" viewBox="0 0 12 20" fill="none" stroke="#fff" stroke-width="1.4"><rect x="1" y="1" width="10" height="18" rx="2"/><path d="M5 16h2"/></svg>
    <div>CALL NOW<br>FOR MORE INFORMATION:</div><strong>666-123-4567</strong>
  </div>
  <div class="cta-divider abs"></div>
  <div class="cta-or abs">OR</div>
  <div class="cta-item abs" style="left:398px">
    <svg width="20" height="15" viewBox="0 0 20 15" fill="none" stroke="#fff" stroke-width="1.3"><rect x="1" y="1" width="18" height="13"/><path d="M1 1l9 7 9-7"/></svg>
    <div>MAIL US NOW<br>FOR ANY QUESTIONS:</div><strong>info@blueharbor.example</strong>
  </div>
</div>

<!-- Footer -->
<footer class="footer abs"></footer>
<div class="f-brand abs"><div class="brand-mark" style="width:20px;height:20px"></div><div class="brand-name">Blue Harbor Real Estate Institute</div></div>
<p class="f-about abs">Lorem ipsum dolor sit amet, consectetur adipiscing elit. Mauris eget rutrum elit. Quisque at orci ut nunc blandit egestas. Pellentesque et purus odio. Nulla ligula magna, vulputate sed elementum quis, vehicula quis enim. Nam eget sem tincidunt, tempus enim ultricies</p>
<div class="social abs" style="left:234px" aria-label="Social profile"></div>
<div class="social abs" style="left:265px" aria-label="Social profile"></div>
<div class="social abs" style="left:297px" aria-label="Social profile"></div>
<div class="social abs" style="left:328px" aria-label="Social profile"></div>

<h4 class="f-head abs" style="left:505px">QUICK LINKS</h4>
<ul class="f-links abs">
  <li>Home</li><li>Information</li><li>Schedule &amp; Cost</li><li>Registration</li><li>About Us</li><li>Location</li><li>Contact</li>
</ul>

<h4 class="f-head abs" style="left:638px">GET IN TOUCH</h4>
<div class="f-contact abs" style="top:2088px">
  <div class="f-ico"><svg width="8" height="11" viewBox="0 0 14 19"><path d="M7 0C3.1 0 0 3.1 0 7c0 5 7 12 7 12s7-7 7-12c0-3.9-3.1-7-7-7zm0 9.5A2.5 2.5 0 1 1 7 4.5a2.5 2.5 0 0 1 0 5z" fill="#fff"/></svg></div>
  <div>4715 Street Name,<br>City, Country - Y123</div>
</div>
<div class="f-contact abs" style="top:2129px">
  <div class="f-ico"><svg width="10" height="10" viewBox="0 0 24 24"><path d="M6.6 10.8a15.1 15.1 0 0 0 6.6 6.6l2.2-2.2c.3-.3.7-.4 1-.2 1.1.4 2.3.6 3.6.6.6 0 1 .4 1 1V20c0 .6-.4 1-1 1A17 17 0 0 1 3 4c0-.6.4-1 1-1h3.5c.6 0 1 .4 1 1 0 1.3.2 2.5.6 3.6.1.3 0 .7-.2 1z" fill="#fff"/></svg></div>
  <div style="padding-top:3px">666-123-4567</div>
</div>
<div class="f-contact abs" style="top:2162px">
  <div class="f-ico"><svg width="10" height="8" viewBox="0 0 20 15"><rect width="20" height="15" fill="#fff"/><path d="M0 0l10 8 10-8" stroke="#555" stroke-width="2" fill="none"/></svg></div>
  <div style="padding-top:3px">info@blueharbor.example</div>
</div>

<h4 class="f-head abs" style="left:797px">NEWSLETTER</h4>
<p class="f-news abs">Enter your email to receive updates and specials</p>
<div class="news-form abs">
  <div class="field"><svg width="10" height="8" viewBox="0 0 20 15" fill="none" stroke="#777" stroke-width="1.5"><rect x="1" y="1" width="18" height="13"/><path d="M1 1l9 7 9-7"/></svg>Email Address</div>
  <div class="send"><svg width="13" height="13" viewBox="0 0 24 24"><path d="M2 11L22 2l-6 20-4-8z" fill="#fff"/></svg></div>
</div>

<div class="footer-bottom abs">Copyright © 2019 Blue Harbor Real Estate Institute. All Rights Reserved</div>

</body>
</html>
```